Torvel, Inc. new buisness cards - brand guide included

We need new business cards. SLEAK SIMPLE FINANCE. They must include a place for NAME, TITLE, CELL, OFFICE PHONE, EMAIL. they also must include our services across the bottom. AIR, OCEAN, FTL, LTL, EXPRESS. for reference this will be being handed to some of the most prestigious shipping companies in a america.

Target Market(s)

Finance and corporate

Contact Information for Business Card

We need new business cards. SLEAK SIMPLE FINANCE. They must include a place for NAME, TITLE, CELL, OFFICE PHONE, EMAIL. they also must include our services across the bottom. AIR, OCEAN, FTL, LTL, EXPRESS.

Requirements
Must have
• We need new business cards. SLEAK SIMPLE FINANCE. They must include a place for NAME, TITLE, CELL, OFFICE PHONE, EMAIL. they also must include our services across the bottom. AIR, OCEAN, FTL, LTL, EXPRESS.
Nice to have
• USE THE COLORS AND LOGO IN THE BRAND GUIDE :)

```html
<!DOCTYPE html>
<html lang="en">
<head>
<meta charset="utf-8">
<title>Torvel, Inc. — Business Cards</title>
<link rel="stylesheet" href="https://fonts.googleapis.com/css2?family=Cinzel:wght@600;700&family=Lato:wght@400;700&display=swap">
<style>
  :root {
    --backdrop: #d6d6d6;
    --card: #1e1e1e;
    --gold: #c3b38b;
    --ink-light: #f1f1f1;
    --serif: "Cinzel", "Times New Roman", serif;
    --sans: "Lato", Arial, sans-serif;
  }
  * { box-sizing: border-box; margin: 0; padding: 0; }
  html, body {
    width: 1200px; height: 1151px; overflow: hidden;
    background: var(--backdrop);
  }
  .stage {
    position: relative; width: 1200px; height: 1151px;
  }
  .card {
    position: absolute; left: 250px; width: 700px; height: 400px;
    background: var(--card);
    box-shadow: 0 10px 30px rgba(0,0,0,.25);
  }
  .card--front { top: 150px; }
  .card--back { top: 610px; }

  .wordmark {
    font-family: var(--serif); font-weight: 600; color: var(--gold);
    letter-spacing: .06em; line-height: 1;
  }
  .card--front .wordmark {
    position: absolute; left: 0; right: 0; top: 128px;
    text-align: center; font-size: 92px;
  }
  .services {
    position: absolute; left: 0; right: 0; bottom: 44px;
    text-align: center; font-family: var(--sans); font-weight: 700;
    font-size: 15px; letter-spacing: .32em; color: var(--ink-light);
  }
  .services .dot { color: var(--gold); margin: 0 .55em 0 .25em; }

  .card--back .wordmark {
    position: absolute; left: 40px; top: 154px; width: 300px;
    text-align: center; font-size: 64px;
  }
  .divider {
    position: absolute; left: 368px; top: 104px; width: 1.5px; height: 210px;
    background: var(--gold);
  }
  .details {
    position: absolute; left: 400px; top: 118px;
  }
  .details__name {
    font-family: var(--serif); font-weight: 700; font-size: 30px;
    color: var(--gold); letter-spacing: .02em; line-height: 1.05;
  }
  .details__title {
    font-family: var(--sans); font-size: 19px; color: var(--ink-light);
    margin-top: 2px;
  }
  .details__company {
    font-family: var(--sans); font-weight: 700; font-size: 16px;
    color: var(--gold); margin-top: 6px;
  }
  .contact { list-style: none; margin-top: 12px; }
  .contact li {
    display: flex; align-items: center; gap: 12px;
    font-family: var(--sans); font-size: 17px; color: var(--ink-light);
    line-height: 26px;
  }
  .contact svg { width: 14px; height: 14px; fill: var(--gold); flex: none; }
</style>
</head>
<body>
<main class="stage">
  <section class="card card--front" aria-label="Card front">
    <div class="wordmark">Torvel</div>
    <p class="services">AIR<span class="dot">•</span>OCEAN<span class="dot">•</span>FTL<span class="dot">•</span>LTL<span class="dot">•</span>EXPRESS</p>
  </section>

  <section class="card card--back" aria-label="Card back">
    <div class="wordmark">Torvel</div>
    <div class="divider"></div>
    <div class="details">
      <h1 class="details__name">DANIEL REYES</h1>
      <p class="details__title">Founder &amp; CEO</p>
      <p class="details__company">Torvel, Inc.</p>
      <ul class="contact">
        <li>
          <svg viewBox="0 0 24 24" aria-hidden="true"><path d="M6.6 10.8c1.4 2.8 3.8 5.1 6.6 6.6l2.2-2.2c.3-.3.7-.4 1-.2 1.1.4 2.3.6 3.6.6.6 0 1 .4 1 1V20c0 .6-.4 1-1 1C10.6 21 3 13.4 3 4c0-.6.4-1 1-1h3.5c.6 0 1 .4 1 1 0 1.3.2 2.5.6 3.6.1.3 0 .7-.2 1z"/></svg>
          (555) 214-0387
        </li>
        <li>
          <svg viewBox="0 0 24 24" aria-hidden="true"><path d="M7 1h10a2 2 0 0 1 2 2v18a2 2 0 0 1-2 2H7a2 2 0 0 1-2-2V3a2 2 0 0 1 2-2zm0 3v14h10V4H7zm5 15.5a1 1 0 1 0 0 2 1 1 0 0 0 0-2z"/></svg>
          (555) 214-0391
        </li>
        <li>
          <svg viewBox="0 0 24 24" aria-hidden="true"><path d="M2 5h20v14H2V5zm2 2v.4l8 5.3 8-5.3V7H4zm16 2.8-8 5.3-8-5.3V17h16V9.8z"/></svg>
          info@torvelfreight.com
        </li>
      </ul>
    </div>
  </section>
</main>
</body>
</html>
```